Website Landing Page for Brightfall Systems

Create a custom designed website landing page for our business. Looking for a professional upscale design that incorporates our logo and logo colors into the theme. I want a standard fixed frame website, not a constant scrolling format that seems to be the trend. To start with I'm looking for more of the graphic design part, maybe a concept or theme, I don't expect to see a finished project. Not interested in generic templates or layouts.

The name of our company is Brightfall Systems and I've attached our logo below. I'd like to have the web page have the same look and feel of our logo, as well as the colors. Our company, Brightfall Systems does system design, installation, and programming, of residential and commercial Audio/Video and Automation systems. We do home theaters, lighting and building automation, video conferencing systems, security camera installations, conference rooms, projectors, distributed audio systems, and similar Technology projects. This will be a professional services/informational website. We will not sell products on this website. This website will be used to advertise our company and communicate our services to prospective customers. Having a well designed, professional and clean website is one way we want to distinguish our company from the competition.

Here are some examples of what I consider a professional well designed website
http://www.qorlamstudio.com/Work/

Last year we had our tradlo store designed (with PixelMarket) and I'm really happy with the way it turned out. You can see it at www.HolvenGearDepot.com I consider this to be a great design and looking for the same level of quality with this new website. However, do not copy or use any part of this design in this new project. This tradlo store is completely separate from our other company Brightfall Systems. I only mention this tradlo store an an example of good work.

Reason: Still going through designs.

Reason: Still working on project and have not had time to review all designs and request revisions.

Reason: Sill going through designs and requesting revisions

Reason: still going through all the submissions we received.

Target Market(s)

People interested in Audio/Video, home theaters, home automation. We do sales, system design, and programming. We typically work on larger projects with both residential and commercial customers.

Industry/Entity Type

Business

Number of Pages Required

1 page

Requirements
Must have
• Great design elements. Please use a white background. I think white goes well with our logo colors.

```html
<!DOCTYPE html>
<html lang="en">
<head>
<meta charset="utf-8">
<title>Brightfall Systems – Landing Page</title>
<link href="https://fonts.googleapis.com/css2?family=Arimo:wght@400;700&display=swap" rel="stylesheet">
<style>
:root{
  --blue:#3f7fcf;
  --blue-dark:#2d64b3;
  --blue-soft:rgba(90,140,210,.72);
  --green:#5cb85c;
  --green-dark:#48a348;
  --sky-top:#3ab4e8;
  --sky-bottom:#3a86d8;
  --ink:#222;
  --white:#fff;
  --header:#efece7;
}
*{box-sizing:border-box;margin:0;padding:0}
html,body{width:1067px;height:1200px;overflow:hidden;background:var(--white)}
body{font-family:"Arimo",Arial,sans-serif;color:var(--ink);position:relative}
.abs{position:absolute}

.site-header{left:32px;top:72px;width:395px;height:25px;background:var(--header);display:flex;align-items:center;padding:0 8px}
.brand{display:flex;align-items:center;gap:4px;font-size:6px;font-weight:700;color:var(--blue);line-height:1}
.brand-dot{width:15px;height:15px;border-radius:50%;border:2px solid var(--blue)}
.phone{margin-left:auto;display:flex;align-items:center;gap:3px;font-size:5px;font-weight:700;color:var(--blue)}
.main-nav{display:flex;gap:8px;margin-left:20px;font-size:5px;font-weight:700;color:var(--blue)}

.hero{left:32px;top:97px;width:395px;height:238px;background:linear-gradient(160deg,#d9cdb9 0%,#b79f7f 45%,#7d6a57 80%,#5a4b3e 100%)}
.hero-panel{left:58px;top:156px;width:100px;height:122px;background:var(--blue-soft);color:var(--white);text-align:center;font-weight:700;text-shadow:0 1px 2px rgba(0,0,0,.4)}
.hero-panel .big{font-size:10px;display:block}
.hero-panel .tiny{font-size:4.5px;display:block;margin:3px 0 8px}
.newsletter{left:337px;top:169px;width:59px}
.newsletter-cta{background:var(--green);color:var(--white);font-size:4.5px;font-weight:700;border-radius:2px;padding:3px 6px;line-height:1.2}
.newsletter-field{background:var(--white);height:11px;margin-top:3px;font-size:3.5px;color:#aaa;text-align:center;line-height:11px;letter-spacing:.5px}

.intro-title{left:32px;top:347px;width:395px;text-align:center;color:var(--green);font-size:16px;font-weight:700}
.intro-text{left:46px;top:369px;width:370px;text-align:justify;text-align-last:center;color:var(--blue);font-size:7.5px;font-weight:700;font-variant:small-caps;line-height:12px;letter-spacing:.2px}

.service{width:115px;text-align:center}
.service-photo{height:72px;display:flex;align-items:center;justify-content:center;color:var(--white);font-weight:700;font-size:8px;letter-spacing:.6px;line-height:9.5px;text-shadow:0 1px 2px #000}
.service-text{font-size:5.2px;line-height:6.8px;margin-top:5px;padding:0 4px}
.service-more{font-size:5.5px;font-weight:700;margin-top:5px}
.tools{display:flex;justify-content:center;gap:4px;margin-top:7px}
.tool{width:22px;text-align:center;font-size:3.5px}
.tool svg{display:block;width:22px;height:22px}

.offer{left:51px;top:579px;width:245px;text-align:center;color:var(--green);font-size:7px;font-weight:700;font-variant:small-caps;letter-spacing:.6px;line-height:10px}
.btn-more{left:322px;top:581px;width:67px;height:16px;border-radius:6px;background:var(--green);color:var(--white);font-size:9px;font-weight:700;font-variant:small-caps;text-align:center;line-height:16px;letter-spacing:.5px}

.quote{width:95px;height:60px}
.quote svg{position:absolute;left:0;top:0;width:100%;height:100%;overflow:visible}
.quote-body{position:absolute;left:4px;top:4px;right:4px;font-size:5.3px;line-height:6.8px;color:var(--blue);font-weight:700;text-align:center}
.quote-by{display:block;text-align:left;font-size:3.8px;margin-top:3px}

.cta-band{left:32px;top:695px;width:395px;height:100px;background:linear-gradient(180deg,#8fa9c8 0%,#cdd8e4 40%,#9aa8a4 70%,#5e7d5c 100%)}
.btn-consult{left:155px;top:729px;width:150px;height:18px;background:var(--green);color:var(--white);font-size:7.5px;font-weight:700;letter-spacing:.8px;text-align:center;line-height:18px;border-radius:2px}

.site-footer{left:32px;top:795px;width:395px;height:65px;background:linear-gradient(180deg,var(--sky-top),var(--sky-bottom));color:var(--white);font-weight:700;font-size:4px}
.social{position:absolute;left:15px;top:16px;display:flex;gap:6px}
.social span{width:11px;height:11px;border-radius:50%;border:1px solid rgba(255,255,255,.7)}
.foot-col{position:absolute;top:11px;text-align:center;line-height:8px;letter-spacing:.3px}
.copyright{position:absolute;left:9px;bottom:7px;font-size:3.3px}
</style>
</head>
<body>

<header class="site-header abs">
  <div class="brand"><span class="brand-dot"></span><span>BRIGHTFALL<br>SYSTEMS</span></div>
  <div class="phone">
    <svg width="8" height="9" viewBox="0 0 8 9"><rect x=".5" y=".5" width="7" height="8" rx="1" fill="none" stroke="#3f7fcf"/><path d="M2.5 2.5c0 2 1 3.5 3 4" stroke="#3f7fcf" fill="none"/></svg>
    555.210.3370
  </div>
  <nav class="main-nav"><span>ABOUT</span><span>GALLERY</span><span>STORE</span><span>CONTACT</span></nav>
</header>

<div class="hero abs" role="img" aria-label="Photo of an upscale living room with a ceiling projector, a wall-mounted screen showing a waterfall and a sectional sofa"></div>
<div class="hero-panel abs">
  <span class="big" style="margin-top:19px">A/V SOLUTIONS</span>
  <span class="tiny">for your</span>
  <span class="big" style="margin-bottom:12px">BUSINESS</span>
  <span class="big" style="margin-bottom:12px">INSTITUTION</span>
  <span class="big">LIFE</span>
</div>
<form class="newsletter abs">
  <div class="newsletter-cta">sign up for our free monthly newsletter</div>
  <div class="newsletter-field">NAME</div>
  <div class="newsletter-field">EMAIL</div>
</form>

<h1 class="intro-title abs">BRIGHTFALL SYSTEMS</h1>
<p class="intro-text abs">Offers the latest in audiovisual technology to enhance your work, play and home. We can design a system for you and we'll back it up with a free 1-year warranty regardless of equipment age, condition or manufacturer warranty remaining.</p>

<section class="service abs" style="left:46px;top:416px">
  <div class="service-photo" role="img" aria-label="Photo of an auditorium with tiered seating and a projection screen" style="background:linear-gradient(180deg,#6a6d72,#3b3f47)">AUDITORIUMS</div>
  <p class="service-text">In order to get sound and visuals PERFECT, many things must be considered. Our products are designed to meet the task</p>
  <p class="service-more">SEE MORE PROJECTS</p>
  <div class="tools">
    <div class="tool"><svg viewBox="0 0 22 22"><rect x=".5" y=".5" width="21" height="21" fill="#fff" stroke="#3f7fcf"/><rect x="4" y="9" width="7" height="6" fill="none" stroke="#3f7fcf"/><rect x="11" y="6" width="7" height="6" fill="none" stroke="#3f7fcf"/></svg>PHOTOS</div>
    <div class="tool"><svg viewBox="0 0 22 22"><rect x=".5" y=".5" width="21" height="21" fill="#fff" stroke="#3f7fcf"/><path d="M1 7h20M1 14h20M7 1v20M14 1v20" stroke="#9cc0e8" stroke-width=".6"/><path d="M5 17l12-12" stroke="#3f7fcf"/></svg>DRAWINGS</div>
    <div class="tool"><svg viewBox="0 0 22 22"><rect x=".5" y=".5" width="21" height="21" fill="#fff" stroke="#3f7fcf"/><rect x="4" y="6" width="14" height="10" fill="none" stroke="#3f7fcf"/><path d="M4 6l7 6 7-6" fill="none" stroke="#3f7fcf"/></svg>CONTACT</div>
  </div>
</section>

<section class="service abs" style="left:172px;top:416px">
  <div class="service-photo" role="img" aria-label="Photo of a conference room with a long table and leather chairs" style="background:linear-gradient(180deg,#8a6a55,#2e2e30)">CONFERENCE<br>ROOMS</div>
  <p class="service-text">Important decisions are made based on information, so clarity and reliability are key.</p>
  <p class="service-more">SEE MORE PROJECTS</p>
  <div class="tools">
    <div class="tool"><svg viewBox="0 0 22 22"><rect x=".5" y=".5" width="21" height="21" fill="#fff" stroke="#3f7fcf"/><rect x="4" y="9" width="7" height="6" fill="none" stroke="#3f7fcf"/><rect x="11" y="6" width="7" height="6" fill="none" stroke="#3f7fcf"/></svg>PHOTOS</div>
    <div class="tool"><svg viewBox="0 0 22 22"><rect x=".5" y=".5" width="21" height="21" fill="#fff" stroke="#3f7fcf"/><path d="M1 7h20M1 14h20M7 1v20M14 1v20" stroke="#9cc0e8" stroke-width=".6"/><path d="M5 17l12-12" stroke="#3f7fcf"/></svg>DRAWINGS</div>
    <div class="tool"><svg viewBox="0 0 22 22"><rect x=".5" y=".5" width="21" height="21" fill="#fff" stroke="#3f7fcf"/><rect x="4" y="6" width="14" height="10" fill="none" stroke="#3f7fcf"/><path d="M4 6l7 6 7-6" fill="none" stroke="#3f7fcf"/></svg>CONTACT</div>
  </div>
</section>

<section class="service abs" style="left:301px;top:416px">
  <div class="service-photo" role="img" aria-label="Photo of a restaurant bar with stools and warm lighting" style="background:linear-gradient(180deg,#3e4a4c,#6b4a34)">RESTAURANTS<br>&amp;<br>CLUBS</div>
  <p class="service-text">Good ambience depends on good equipment and design.</p>
  <p class="service-more">SEE MORE PROJECTS</p>
  <div class="tools">
    <div class="tool"><svg viewBox="0 0 22 22"><rect x=".5" y=".5" width="21" height="21" fill="#fff" stroke="#3f7fcf"/><rect x="4" y="9" width="7" height="6" fill="none" stroke="#3f7fcf"/><rect x="11" y="6" width="7" height="6" fill="none" stroke="#3f7fcf"/></svg>PHOTOS</div>
    <div class="tool"><svg viewBox="0 0 22 22"><rect x=".5" y=".5" width="21" height="21" fill="#fff" stroke="#3f7fcf"/><path d="M1 7h20M1 14h20M7 1v20M14 1v20" stroke="#9cc0e8" stroke-width=".6"/><path d="M5 17l12-12" stroke="#3f7fcf"/></svg>DRAWINGS</div>
    <div class="tool"><svg viewBox="0 0 22 22"><rect x=".5" y=".5" width="21" height="21" fill="#fff" stroke="#3f7fcf"/><rect x="4" y="6" width="14" height="10" fill="none" stroke="#3f7fcf"/><path d="M4 6l7 6 7-6" fill="none" stroke="#3f7fcf"/></svg>CONTACT</div>
  </div>
</section>

<p class="offer abs">Along with system design, we offer programming services, project management and even technical drawings</p>
<a class="btn-more abs">See More</a>

<blockquote class="quote abs" style="left:56px;top:612px">
  <svg viewBox="0 0 95 60"><path d="M6 1h83a5 5 0 0 1 5 5v36a5 5 0 0 1-5 5H80l-6 11 -1-11H6a5 5 0 0 1-5-5V6a5 5 0 0 1 5-5z" fill="#fff" stroke="#3f7fcf" stroke-width=".8"/></svg>
  <p class="quote-body">“ Our control room is now the peak of efficiency thanks to a great design by Brightfall Systems. We Love it.”<span class="quote-by">Dan Reyes – Lakeview Transit System</span></p>
</blockquote>
<blockquote class="quote abs" style="left:178px;top:608px">
  <svg viewBox="0 0 95 60"><path d="M6 1h83a5 5 0 0 1 5 5v36a5 5 0 0 1-5 5H80l-6 11 -1-11H6a5 5 0 0 1-5-5V6a5 5 0 0 1 5-5z" fill="#fff" stroke="#3f7fcf" stroke-width=".8"/></svg>
  <p class="quote-body">“ Customers are complimenting us now on the quality of the music we play during the day”<span class="quote-by">Mara Quinn – Corner Mug Cafe</span></p>
</blockquote>
<blockquote class="quote abs" style="left:307px;top:612px">
  <svg viewBox="0 0 95 60"><path d="M6 1h83a5 5 0 0 1 5 5v36a5 5 0 0 1-5 5H80l-6 11 -1-11H6a5 5 0 0 1-5-5V6a5 5 0 0 1 5-5z" fill="#fff" stroke="#3f7fcf" stroke-width=".8"/></svg>
  <p class="quote-body">“ Our meetings come across as more professional now. We like inviting customers to our sessions”<span class="quote-by">Leo Hart – Pellam Corp</span></p>
</blockquote>

<div class="cta-band abs" role="img" aria-label="Photo of a city skyline across a river under a cloudy blue sky"></div>
<a class="btn-consult abs">BOOK A FREE CONSULTATION</a>

<footer class="site-footer abs">
  <div class="social"><span></span><span></span><span></span></div>
  <div class="foot-col" style="left:92px">TERMS &amp; CONDITIONS<br>PRIVACY POLICY<br>WARRANTY</div>
  <div class="foot-col" style="left:186px">ABOUT<br>GALLERY<br>STORE<br>CONTACT<br>BLOG</div>
  <div class="foot-col" style="left:250px">AUDITORIUMS<br>CONFERENCE ROOMS<br>RESTAURANTS CLUBS<br>AUTOMATION<br>CCTV</div>
  <div class="foot-col" style="left:335px;width:56px">BRIGHTFALL SYSTEMS<br><br>2210 N Harlow Ave<br>Riverton, IN 46201<br><span style="font-size:5px">555.210.3370</span></div>
  <div class="copyright">COPYRIGHT 2017 BRIGHTFALL SYSTEMS</div>
</footer>

</body>
</html>
```